Personal Training Studio needs small flyer design

My Personal Training Studio is looking to offer local high end clothes shops the option to offer their customers free Personal Training at our studio. It will be a small flyer (more a slip - landscape) that can be put into customers shopping bags once they have purchased an item from the store.
It is being marketed as a Local Fitness Initiative which is called "Be Fit In Your Clothes" The idea is to come from a "Be Fit" health perspective but also "Fit into your clothes" from the clothes shops perspective. Perhaps the "Be" in a different colour to the rest of the title. I would like my company logo and colours to be used, plus the address of the of the studio (see website - www.harbourlane7gym.co.uk). Flyer can be double sided

Target Market(s)

High end clothing shops

Industry/Entity Type

Training

Requirements
Must have
• Reference to the fact that the voucher is offering a FREE Personal Training session. Contact us to book yours today.

```html
<!DOCTYPE html>
<html lang="en">
<head>
<meta charset="utf-8">
<title>Be Fit In Your Clothes – Harbour Lane 7 Gym</title>
<link rel="stylesheet" href="https://fonts.googleapis.com/css2?family=Cinzel:wght@400;600&family=Roboto+Condensed:wght@400;700&display=swap">
<style>
  :root {
    --page-bg: #5b5e64;
    --teal: #4bbfc4;
    --teal-dark: #3aa9ae;
    --navy: #2b2d6e;
    --white: #ffffff;
    --ink-dark: #1b1c1f;
    --photo-light: #e9ebec;
    --photo-mid: #9a9ea2;
    --skin: #b99a86;
  }
  * { box-sizing: border-box; margin: 0; padding: 0; }
  html, body { width: 1200px; height: 1000px; overflow: hidden; }
  body { background: var(--page-bg); position: relative; font-family: "Roboto Condensed", sans-serif; }

  .flyer {
    position: absolute; left: 47px; top: 233px;
    width: 1106px; height: 520px; overflow: hidden;
    box-shadow: 0 6px 18px rgba(0,0,0,.35);
  }
  .gym-photo {
    position: absolute; inset: 0;
    background:
      linear-gradient(180deg, rgba(0,0,0,0) 45%, rgba(20,21,24,.85) 72%, var(--ink-dark) 100%),
      linear-gradient(90deg, #f3f4f4 0%, var(--photo-light) 40%, #d8dadb 70%, #eceeee 100%);
  }
  .gym-photo::after {
    content: ""; position: absolute; left: 160px; right: 150px; top: 150px; height: 130px;
    background: linear-gradient(180deg, rgba(120,124,128,.25), rgba(60,62,66,.55));
    filter: blur(14px);
  }
  .athlete-photo {
    position: absolute; left: 0; top: 0; width: 360px; height: 520px;
    background:
      linear-gradient(90deg, rgba(0,0,0,0) 55%, rgba(233,235,236,0) 100%),
      radial-gradient(ellipse 140px 260px at 110px 250px, var(--skin) 0%, #8d7466 55%, rgba(60,58,58,.0) 100%),
      linear-gradient(180deg, #6a6560 0%, #4d4a48 60%, #2b2a2a 100%);
    -webkit-mask-image: linear-gradient(90deg, #000 55%, transparent 100%);
            mask-image: linear-gradient(90deg, #000 55%, transparent 100%);
  }

  .brand-panel {
    position: absolute; left: 452px; top: 0; width: 202px; height: 100px;
    background: var(--navy);
    display: flex; flex-direction: column; align-items: center; justify-content: center;
    color: var(--white); font-weight: 400; text-align: center; line-height: 1.05;
    font-size: 26px; letter-spacing: 1px; text-transform: uppercase;
  }

  .offer-badge {
    position: absolute; left: 826px; top: 61px; width: 220px; height: 220px;
    border-radius: 50%; background: var(--teal);
    box-shadow: 0 0 0 4px rgba(255,255,255,.0);
    display: flex; flex-direction: column; align-items: center; justify-content: center;
    color: var(--white); text-align: center;
  }
  .offer-badge::before {
    content: ""; position: absolute; inset: 8px; border: 2px solid var(--white); border-radius: 50%;
  }
  .offer-badge__free { font-weight: 700; font-size: 68px; line-height: 1; margin-top: -6px; }
  .offer-badge__label { font-size: 27px; line-height: 1.1; margin-top: 8px; }

  .headline {
    position: absolute; left: 0; right: 0; top: 300px; text-align: center;
    font-family: "Cinzel", serif; font-weight: 400; font-size: 62px; line-height: 1;
    color: var(--white); letter-spacing: -1px; padding-left: 30px;
  }
  .headline__accent { color: var(--teal); }
  .subline {
    position: absolute; left: 0; right: 0; top: 366px; text-align: center; padding-left: 30px;
    color: var(--white); font-size: 25px;
  }
  .subline strong { font-weight: 700; }

  .contact-band {
    position: absolute; left: 0; right: 0; top: 410px; height: 45px;
    background: var(--teal); border-top: 1px solid #cfd9b0;
    display: flex; align-items: center; justify-content: center; gap: 42px;
    color: var(--white); font-size: 22px; padding-left: 30px;
  }
  .contact-band__item { display: flex; align-items: center; gap: 6px; white-space: nowrap; }
  .contact-band svg { fill: var(--white); display: block; }

  .web-address {
    position: absolute; left: 0; right: 0; top: 466px; text-align: center;
    font-size: 27px; color: var(--white); letter-spacing: -.5px;
  }
  .web-address__name { color: var(--teal); font-weight: 700; }
</style>
</head>
<body>
  <section class="flyer">
    <div class="gym-photo" role="img" aria-label="Bright personal training studio with dumbbell racks, squat racks and suspension trainers"></div>
    <div class="athlete-photo" role="img" aria-label="Woman in a grey sports top wiping her forehead with a towel after training"></div>

    <div class="brand-panel">Harbour Lane 7<br>Gym</div>

    <div class="offer-badge">
      <span class="offer-badge__free">FREE</span>
      <span class="offer-badge__label">Personal Training<br>Session</span>
    </div>

    <h1 class="headline">Be FIT <span class="headline__accent">In Your Clothes</span></h1>
    <p class="subline">Contact us to book your <strong>FREE</strong> personal training session today!</p>

    <div class="contact-band">
      <span class="contact-band__item">
        <svg width="20" height="28" viewBox="0 0 20 28"><path d="M10 0C4.5 0 0 4.4 0 9.8 0 17 10 28 10 28s10-11 10-18.2C20 4.4 15.5 0 10 0zm0 14a4.2 4.2 0 1 1 0-8.4 4.2 4.2 0 0 1 0 8.4z"/></svg>
        7 Harbour Lane, Whitby, North Yorkshire
      </span>
      <span class="contact-band__item">
        <svg width="24" height="28" viewBox="0 0 24 28"><path d="M6 1l4 6-3 3c1.5 4 4.5 7.5 8 9.5l3-3 6 4-3 5C11 25 1 14 1 5z"/></svg>
        01632 960 418
      </span>
      <span class="contact-band__item">
        <svg width="40" height="26" viewBox="0 0 40 26"><path d="M0 0h40v26H0z" fill="none" stroke="#fff" stroke-width="2.5"/><path d="M1 1l19 14L39 1M1 25l14-12M39 25L25 13" fill="none" stroke="#fff" stroke-width="2.5"/></svg>
        info@harbourlane7gym.co.uk
      </span>
    </div>

    <p class="web-address"><span class="web-address__name">HarbourLane7Gym</span>.co.uk</p>
  </section>
</body>
</html>
```